High-End audio shop owner needs a business card

I need a personal Business Card for my Audio shop which exists since 1962. We offer high Quality brands, professional Attention and run our own repair-service-department. I look for a design which will be printed on high Quality paper and shall convey trust to the Client that we are very serious. Language is german.

```html
<!DOCTYPE html>
<html lang="de">
<head>
<meta charset="utf-8">
<title>Hi-Fi Lindqvist – Visitenkarte</title>
<link rel="stylesheet" href="https://fonts.googleapis.com/css2?family=Lato:wght@400;700;900&display=swap">
<style>
  :root {
    --backdrop: #1b1c1f;
    --card: #25282b;
    --card-edge: #2d3034;
    --silver: #7d8084;
    --orange: #f26a1b;
    --ink-light: #d6d7d9;
  }
  html, body {
    margin: 0;
    padding: 0;
    width: 1200px;
    height: 800px;
    overflow: hidden;
    background: var(--backdrop);
    font-family: "Lato", Arial, sans-serif;
  }
  .stage {
    position: relative;
    width: 1200px;
    height: 800px;
    display: flex;
    align-items: center;
    justify-content: center;
    gap: 50px;
  }
  .card {
    position: relative;
    width: 520px;
    height: 300px;
    background: var(--card);
    border: 1px solid var(--card-edge);
    border-radius: 22px;
    box-shadow: 0 24px 50px rgba(0,0,0,0.55);
    overflow: hidden;
  }
  .brand-name {
    font-weight: 900;
    text-transform: uppercase;
    letter-spacing: 0.02em;
    white-space: nowrap;
  }
  /* front side */
  .card-front .brand-name {
    position: absolute;
    left: 0;
    right: 0;
    top: 50%;
    transform: translateY(-50%);
    text-align: center;
    font-size: 44px;
    color: var(--silver);
  }
  /* back side */
  .card-back .brand-name {
    position: absolute;
    left: 34px;
    bottom: 70px;
    font-size: 25px;
    color: var(--orange);
  }
  .divider {
    position: absolute;
    left: 272px;
    top: 52px;
    width: 1px;
    height: 196px;
    background: var(--orange);
  }
  .contact {
    position: absolute;
    left: 294px;
    top: 56px;
    color: var(--ink-light);
    font-size: 12.5px;
    line-height: 1.45;
  }
  .person-name {
    margin: 0;
    color: var(--orange);
    font-size: 17px;
    font-weight: 700;
    text-transform: uppercase;
    letter-spacing: 0.02em;
  }
  .person-role {
    margin: 0 0 16px;
    font-size: 13px;
  }
  .address { margin: 0 0 14px; }
  .contact-list {
    list-style: none;
    margin: 0;
    padding: 0;
  }
  .contact-list li {
    display: flex;
    align-items: center;
    gap: 8px;
  }
  .contact-list svg {
    width: 11px;
    height: 11px;
    fill: var(--orange);
    flex: none;
  }
</style>
</head>
<body>
<main class="stage">
  <section class="card card-front">
    <div class="brand-name">Hi-Fi Lindqvist</div>
  </section>

  <section class="card card-back">
    <div class="brand-name">Hi-Fi Lindqvist</div>
    <div class="divider"></div>
    <div class="contact">
      <p class="person-name">Karl Brenner</p>
      <p class="person-role">Director</p>
      <p class="address">Postfach 45, Lindenallee 12<br>20095 Hamburg</p>
      <ul class="contact-list">
        <li>
          <svg viewBox="0 0 12 12" aria-hidden="true"><path d="M2.5 1h2l1 2.6-1.3 1a6 6 0 0 0 3.2 3.2l1-1.3L11 7.5v2c0 .8-.7 1.5-1.5 1.5A8.5 8.5 0 0 1 1 2.5C1 1.7 1.7 1 2.5 1z"/></svg>
          (040) 318 2264
        </li>
        <li>
          <svg viewBox="0 0 12 12" aria-hidden="true"><path d="M1 2.5h10v7H1z M1 2.5l5 4 5-4" /></svg>
          info@lindqvist-audio.de
        </li>
        <li>
          <svg viewBox="0 0 12 12" aria-hidden="true"><circle cx="6" cy="6" r="5"/></svg>
          www.lindqvist-audio.de
        </li>
      </ul>
    </div>
  </section>
</main>
</body>
</html>
```